Trifold brochure

Need a trifold marketing brochure for my autism therapy for children business . I would be interested in having designs in both English and Spanish if possible!!!!! Website is www.quillmeadowtherapy.com
Address on brochure needs to be 2736 Larkspur Ave W Suite 5
Minneapolis, MN 55719
Updates
Can you update the address on brochure to 2736 Larkspur Ave W Suite 5
Minneapolis, MN 55719
Target Market(s)
Autism therapy for children
Industry/Entity Type
Autism Therapy
Look and feel

```html
<!DOCTYPE html>
<html lang="en">
<head>
<meta charset="utf-8">
<title>Quill Meadow Therapy – Trifold Brochure</title>
<link rel="stylesheet" href="https://fonts.googleapis.com/css2?family=Montserrat:wght@400;500;600;700;800;900&family=Oswald:wght@600&display=swap">
<style>
  :root{
    --blue:#1d5ca3;
    --navy:#17407e;
    --gold:#b07a2d;
    --white:#ffffff;
    --mist:#eceef1;
    --ink:#4a4f57;
    --stage:#e4e5e7;
  }
  *{box-sizing:border-box;margin:0;padding:0}
  html,body{width:1200px;height:900px;overflow:hidden;background:var(--stage);font-family:'Montserrat',sans-serif}
  .spread{position:absolute;top:225px;width:580px;height:450px;display:grid;grid-template-columns:repeat(3,1fr);box-shadow:0 6px 18px rgba(0,0,0,.18)}
  .spread--outside{left:13px}
  .spread--inside{left:607px}
  .panel{position:relative;overflow:hidden;background:var(--white)}
  .panel > svg.bg{position:absolute;inset:0;width:100%;height:100%}
  .layer{position:absolute;left:0;right:0}
  .center{text-align:center}

  /* About */
  .about{left:22px;right:20px;top:22px}
  .about h2{font-size:16px;font-weight:600;color:var(--blue);line-height:1}
  .about h2 em{display:block;font-style:italic;font-weight:800;color:var(--gold);font-size:16px;margin-top:2px}
  .about .rule{width:50px;height:2px;background:var(--gold);margin:3px 0 8px}
  .about p{font-size:5.8px;line-height:1.6;color:var(--ink)}

  /* Contact */
  .contact{top:46px}
  .contact .kicker{font-size:8.5px;font-weight:700;color:var(--blue)}
  .contact h2{font-size:22px;font-weight:900;color:var(--gold);line-height:1.05}
  .contact .rule{width:32px;height:2px;background:var(--blue);margin:5px auto 10px}
  .contact .item{font-size:7px;color:#333;margin-bottom:8px;line-height:1.35}
  .contact .item svg{display:block;margin:0 auto 3px}
  .hours{top:375px;color:var(--white)}
  .hours h3{font-size:7.5px;font-weight:700;margin-bottom:3px}
  .hours p{font-size:7px;font-weight:500;line-height:1.6}

  /* Cover */
  .brand{top:30px;font-size:9px;font-weight:700;color:var(--blue);letter-spacing:.3px}
  .brand::before{content:"";display:block;width:8px;height:8px;border-radius:50%;background:var(--blue);margin:0 auto 4px}
  .cover-text{top:284px;left:10px;right:10px;color:var(--white)}
  .cover-text .l1{font-size:15px;font-weight:700;letter-spacing:.5px}
  .cover-text .l2{font-size:25px;font-weight:900;color:var(--gold);line-height:1}
  .cover-text .l3{font-size:8.5px;font-weight:700;margin-top:3px}
  .cover-text .rule{width:30px;height:2px;background:var(--gold);margin:5px auto 7px}
  .cover-text p{font-size:5.6px;line-height:1.45}

  /* Services */
  .badge-text{top:138px;font-family:'Oswald',sans-serif;font-weight:600;color:var(--white);font-size:15px;line-height:1.15;letter-spacing:.5px}
  .services{top:268px;left:14px;right:10px}
  .service{display:flex;gap:8px;margin-bottom:12px}
  .service .num{flex:0 0 22px;height:22px;border-radius:50%;background:var(--navy);color:var(--white);font-weight:800;font-size:9px;display:flex;align-items:center;justify-content:center}
  .service h4{font-size:6.6px;font-weight:700;color:var(--navy);line-height:1.2}
  .service h4 span{color:var(--gold)}
  .service p{font-size:4.6px;line-height:1.45;color:var(--ink);margin-top:2px}

  /* Value */
  .value{top:28px;left:14px;right:14px}
  .value h2{font-size:15px;font-weight:900;color:var(--gold)}
  .value h3{font-size:8.5px;font-weight:700;color:var(--blue);line-height:1.25}
  .value .rule{width:32px;height:2px;background:var(--gold);margin:7px auto 8px}
  .value p{font-size:5.6px;line-height:1.4;color:var(--ink)}
  .statements{top:230px;left:20px;right:18px;color:var(--white)}
  .statements h4{font-size:8px;font-weight:700;margin-bottom:2px}
  .statements h4 span{color:var(--gold)}
  .statements p{font-size:4.7px;line-height:1.45;margin-bottom:12px}

  /* How we do */
  .how{top:218px;left:22px;right:16px}
  .how h2{font-size:16px;font-weight:900;color:var(--navy);line-height:1.15}
  .how h2 span{color:var(--gold)}
  .how p{font-size:5.8px;line-height:1.45;color:var(--ink);margin-top:6px}
</style>
</head>
<body>

<section class="spread spread--outside">

  <article class="panel panel--about">
    <svg class="bg" viewBox="0 0 193 450" preserveAspectRatio="none">
      <polygon points="0,300 193,370 193,450 0,450" fill="var(--blue)"/>
      <rect x="0" y="28" width="4" height="240" fill="var(--gold)"/>
      <polygon points="14,14 178,8 178,230 98,280 14,230" fill="var(--white)" stroke="var(--gold)" stroke-width="1.2"/>
      <path role="img" aria-label="Photo of a smiling therapist and young girl stacking colourful blocks" d="M0,330 Q40,270 95,275 Q150,280 170,330 L172,450 L0,450 Z" fill="#e9a49c"/>
    </svg>
    <div class="layer about">
      <h2>About <em>ABA Therapy</em></h2>
      <div class="rule"></div>
      <p>ABA Therapy Applied Behavioral Analysis (ABA) Therapy is endorsed by national health advisors and leading children's health councils and has been scientifically proven to be the most effective in helping a child with autism to acquire the necessary skills to reach their full potential. Research has proven that early diagnosis and intervention are key to achieving success, as well as a commitment to the individualized treatment plan developed specifically for your child by one of our expert Clinicians.</p>
    </div>
  </article>

  <article class="panel panel--contact">
    <svg class="bg" viewBox="0 0 193 450" preserveAspectRatio="none">
      <polygon points="0,340 193,230 193,450 0,450" fill="var(--blue)"/>
      <polygon role="img" aria-label="Street map showing the clinic location" points="48,240 150,285 150,385 48,340" fill="#eef1f3" stroke="var(--gold)" stroke-width="2"/>
    </svg>
    <div class="layer contact center">
      <div class="kicker">Get in touch</div>
      <h2>Contact</h2>
      <div class="rule"></div>
      <div class="item">
        <svg width="11" height="11" viewBox="0 0 12 12"><circle cx="6" cy="6" r="6" fill="var(--gold)"/><path d="M4 3.2l1 .1.5 1.5-.7.6a4 4 0 0 0 1.8 1.8l.6-.7 1.5.5.1 1A1 1 0 0 1 7.8 9 5 5 0 0 1 3 4.2a1 1 0 0 1 1-1z" fill="#fff"/></svg>
        612-555-0148
      </div>
      <div class="item">
        <svg width="11" height="11" viewBox="0 0 12 12"><circle cx="6" cy="6" r="6" fill="var(--gold)"/><rect x="3" y="4" width="6" height="4.2" fill="#fff"/><path d="M3 4l3 2.2L9 4" stroke="var(--gold)" stroke-width=".6" fill="none"/></svg>
        hello@quillmeadowtherapy.com
      </div>
      <div class="item">
        <svg width="11" height="11" viewBox="0 0 12 12"><circle cx="6" cy="6" r="6" fill="var(--gold)"/><path d="M6 2.6a2.2 2.2 0 0 1 2.2 2.2C8.2 6.6 6 9.2 6 9.2S3.8 6.6 3.8 4.8A2.2 2.2 0 0 1 6 2.6z" fill="#fff"/><circle cx="6" cy="4.8" r=".8" fill="var(--gold)"/></svg>
        2736 Larkspur Ave W Suite 5<br>Minneapolis, MN 55719
      </div>
    </div>
    <div class="layer hours center">
      <h3>Opening Hours</h3>
      <p>Monday - Friday | 9 am- 8 pm<br>Saturday - Sunday | 9 am-5 pm</p>
    </div>
  </article>

  <article class="panel panel--cover">
    <svg class="bg" viewBox="0 0 193 450" preserveAspectRatio="none">
      <rect width="193" height="450" fill="var(--mist)"/>
      <polygon points="0,230 96,275 193,230 193,450 0,450" fill="var(--blue)"/>
      <polygon points="14,40 28,30 28,60" fill="var(--gold)"/>
      <polygon points="179,40 165,30 165,60" fill="var(--gold)"/>
      <polygon points="34,220 96,250 159,220 159,232 96,262 34,232" fill="var(--gold)"/>
      <polygon role="img" aria-label="Photo of a therapist reading with a young boy" points="14,70 96,105 179,70 179,205 96,245 14,205" fill="#d9d4cc"/>
    </svg>
    <div class="layer brand center">QUILL MEADOW</div>
    <div class="layer cover-text center">
      <div class="l1">BUILDING</div>
      <div class="l2">BRIDGES</div>
      <div class="l3">TO BRIGHTER FUTURES</div>
      <div class="rule"></div>
      <p>Discovering the Unique Potential of Every Child through Compassionate, Evidence-Based Autism Therapy, Fostering Growth, Connection, and Confidence.</p>
    </div>
  </article>
</section>

<section class="spread spread--inside">

  <article class="panel panel--services">
    <svg class="bg" viewBox="0 0 193 450" preserveAspectRatio="none">
      <rect width="193" height="450" fill="var(--mist)"/>
      <polygon role="img" aria-label="Blue-toned photo of a child working with a therapist" points="0,0 193,0 193,150 96,205 0,150" fill="#2c68ad"/>
      <polygon points="36,72 96,95 157,72 157,165 96,198 36,165" fill="var(--gold)"/>
      <polygon points="28,200 96,232 165,200 165,210 96,242 28,210" fill="var(--gold)"/>
      <polygon points="38,218 96,246 155,218 155,226 96,254 38,226" fill="var(--navy)"/>
    </svg>
    <div class="layer badge-text center">OUR<br>SERVICES</div>
    <div class="layer services">
      <div class="service"><div class="num">01</div><div><h4><span>ABA</span> Therapy</h4><p>Our ABA therapy focuses on enhancing communication, social skills, and behavior management in children with autism spectrum disorder (ASD).</p></div></div>
      <div class="service"><div class="num">02</div><div><h4><span>Speech and</span> Language Therapy</h4><p>Our speech and language therapy services aim to improve communication, expressive language, and social interaction abilities in children with autism.</p></div></div>
      <div class="service"><div class="num">03</div><div><h4><span>Occupational</span> Therapy (OT)</h4><p>Occupational therapy at Quill Meadow targets the development of fine motor skills, sensory processing abilities, and self-care capabilities in children with autism.</p></div></div>
    </div>
  </article>

  <article class="panel panel--value">
    <svg class="bg" viewBox="0 0 193 450" preserveAspectRatio="none">
      <polygon points="0,150 193,225 193,450 0,450" fill="var(--navy)"/>
      <polygon points="193,155 193,225 140,205" fill="var(--gold)"/>
      <polygon points="60,150 90,167 90,201 60,218 30,201 30,167" fill="var(--white)" stroke="var(--gold)" stroke-width="1.5"/>
      <polygon role="img" aria-label="Photo of a therapist playing with a child" points="60,155 86,170 86,198 60,213 34,198 34,170" fill="#e0b26f"/>
    </svg>
    <div class="layer value center">
      <h2>Our Value</h2>
      <h3>Quality Care From Quality Experts.</h3>
      <div class="rule"></div>
      <p>At Quill Meadow, our values drive our mission. We provide compassionate, evidence-based therapy for children with autism, focusing on individualized care and early intervention in a nurturing environment.</p>
    </div>
    <div class="layer statements">
      <h4>Our <span>Vision</span></h4>
      <p>To envision and strive towards a future where every child diagnosed with autism is supported, empowered, and equipped to achieve their fullest potential, fostering inclusivity and acceptance.</p>
      <h4>Our <span>Mission</span></h4>
      <p>We're dedicated to providing personalized, evidence-based therapy for every child with autism. Through early intervention and compassionate care, we empower growth and confidence, fostering thriving futures.</p>
      <h4>Our <span>Motto</span></h4>
      <p>Unlocking Potential, Building Bridges, Illuminating Futures: Together, We Build Brighter Tomorrows.</p>
    </div>
  </article>

  <article class="panel panel--how">
    <svg class="bg" viewBox="0 0 193 450" preserveAspectRatio="none">
      <rect width="193" height="450" fill="var(--white)"/>
      <polygon points="30,0 193,0 193,120 100,205 30,180" fill="var(--blue)"/>
      <polygon points="0,60 14,66 14,140 0,135" fill="var(--gold)"/>
      <polygon points="193,140 193,190 150,190" fill="var(--gold)"/>
      <polygon points="18,28 96,46 180,18 180,160 96,200 18,168" fill="var(--white)"/>
      <polygon role="img" aria-label="Photo of children playing with blocks at a table" points="26,40 96,56 172,30 172,154 96,190 26,160" fill="#c9b9a0"/>
      <polygon points="0,395 0,450 120,450" fill="var(--gold)"/>
    </svg>
    <div class="layer how">
      <h2>HOW<br>WE DO<br><span>ABA THERAPY</span></h2>
      <p>Quill Meadow offers a safe and clean center-based environment, led by highly-trained clinicians. Our team of experienced certified behavior analysts and trained behavior technicians work with you and your child to develop individualized treatment plans based on their unique needs. We consider your child's needs and wants throughout the entire process. We prepare children for succeeding in all aspects of their life.</p>
    </div>
  </article>
</section>

</body>
</html>
```